Consulting company needs Business Cards - rough concept provided

I'm looking for someone to take our business card idea and make is slick and polished - to communicate our high-end, sophisticated, serious consulting business. We have a rough layout we did in-house. We are open to ideas on repo-ing elements, adjusting sizes, typefaces etc... within the general concept we've already come up with. We want it to be super-clean and sophisticated. We want to keep the white backgrounds, and blue brand colors. Our goal is to print with painted blue edges on thick cardstock. Thank you!!

```html
<!DOCTYPE html>
<html lang="en">
<head>
<meta charset="utf-8">
<title>Northvale Consulting – Stationery</title>
<link rel="stylesheet" href="https://fonts.googleapis.com/css2?family=Open+Sans:wght@400;600;700&display=swap">
<style>
  :root {
    --bg: #eeeff1;
    --paper: #fbfbfa;
    --blue: #1e6fd0;
    --blue-deep: #0f4fb8;
    --blue-soft: #dbe8f8;
    --ink: #5b5f66;
  }
  * { box-sizing: border-box; margin: 0; padding: 0; }
  html, body { width: 1200px; height: 800px; overflow: hidden; }
  body { background: var(--bg); font-family: "Open Sans", sans-serif; color: var(--ink); position: relative; }
  .sheet { position: absolute; background: var(--paper); overflow: hidden; }
  .brand { font-weight: 700; color: var(--blue); letter-spacing: -0.01em; line-height: 1; position: relative; }
  .artwork { position: absolute; background: linear-gradient(135deg, var(--blue-soft) 0%, #7fb0ea 55%, var(--blue-deep) 100%); }

  .letterhead { left: 38px; top: 38px; width: 529px; height: 710px; }
  .letterhead .brand { position: absolute; left: 41px; top: 40px; font-size: 42px; }
  .letterhead .tagline { position: absolute; left: 374px; top: 52px; padding-left: 14px; border-left: 1px solid var(--blue);
    font-size: 8.5px; font-weight: 600; color: var(--blue); letter-spacing: 0.04em; line-height: 1.45; }
  .letterhead .artwork { left: 210px; top: 430px; width: 319px; height: 280px; }
  .letterhead .footer { position: absolute; left: 41px; top: 580px; font-size: 8.5px; line-height: 1.6; }
  .footer .short-rule { width: 18px; height: 1px; background: var(--blue); margin-bottom: 8px; }
  .footer .company { font-weight: 600; color: var(--blue-deep); letter-spacing: 0.03em; }
  .footer .motto { color: var(--blue-deep); margin-bottom: 8px; }
  .footer .address { margin-bottom: 8px; }
  .footer .web, .env-front .web { color: var(--blue-deep); }

  .env-front { left: 609px; top: 35px; width: 557px; height: 254px; }
  .env-front .brand { position: absolute; left: 40px; top: 37px; font-size: 31px; }
  .env-front .address { position: absolute; left: 42px; top: 90px; font-size: 8.5px; line-height: 1.6; }
  .env-front .web { position: absolute; left: 42px; top: 124px; font-size: 8.5px; }
  .env-front .artwork { left: 300px; top: 70px; width: 257px; height: 184px; }

  .env-back { left: 609px; top: 318px; width: 557px; height: 235px; }
  .env-back svg { position: absolute; inset: 0; }

  .card { position: absolute; top: 586px; height: 155px; background: var(--paper);
    border-left: 3px solid var(--blue-deep); border-bottom: 3px solid var(--blue-deep); overflow: hidden; }
  .card-front { left: 609px; width: 243px; text-align: center; }
  .card-front .brand { font-size: 28px; margin-top: 50px; }
  .card-front .short-rule { width: 18px; height: 1px; background: var(--blue); margin: 10px auto 12px; }
  .card-front .tagline { font-size: 7px; font-weight: 600; color: var(--blue); letter-spacing: 0.05em; }

  .card-back { left: 882px; width: 284px; }
  .card-back .artwork { left: 195px; top: 0; width: 86px; height: 152px; }
  .card-back .details { position: absolute; left: 26px; top: 26px; }
  .card-back .name { font-size: 11.5px; font-weight: 600; color: var(--blue-deep); letter-spacing: 0.05em; }
  .card-back .role { font-size: 7px; color: var(--blue); letter-spacing: 0.04em; margin: 3px 0 14px; }
  .contact { list-style: none; font-size: 7px; line-height: 1.45; }
  .contact li { display: flex; gap: 8px; margin-bottom: 7px; }
  .contact svg { width: 8px; height: 8px; flex: none; margin-top: 1px; }
  .contact .web { color: var(--blue-deep); }
</style>
</head>
<body>
<section class="sheet letterhead">
  <div class="artwork" role="img" aria-label="Flowing blue ribbon artwork"></div>
  <div class="brand">NORTHVALE</div>
  <div class="tagline">STRATEGY. INTELLIGENCE.<br>GROWTH.</div>
  <div class="footer">
    <div class="short-rule"></div>
    <div class="company">NORTHVALE CONSULTING</div>
    <div class="motto">Strategy. Intelligence. Growth.</div>
    <div class="address">480 Harlow Street<br>Boston, MA 02116</div>
    <div class="web">northvale.com</div>
  </div>
</section>

<section class="sheet env-front">
  <div class="artwork" role="img" aria-label="Flowing blue ribbon artwork"></div>
  <div class="brand">NORTHVALE</div>
  <div class="address">480 Harlow Street<br>Boston, MA 02116</div>
  <div class="web">northvale.com</div>
</section>

<section class="sheet env-back">
  <svg viewBox="0 0 557 235" role="img" aria-label="Envelope flap printed with blue ribbon artwork">
    <defs>
      <linearGradient id="flap" x1="0" y1="0" x2="1" y2="1">
        <stop offset="0" stop-color="#7fb0ea"/>
        <stop offset="1" stop-color="#0f4fb8"/>
      </linearGradient>
    </defs>
    <path d="M0,235 L240,120 M557,235 L330,120" fill="none" stroke="#e2e4e8" stroke-width="0.8"/>
    <path d="M0,0 L557,0 L548,30 C538,55 510,72 470,90 L345,150 C318,162 290,162 262,150 L40,58 C15,48 4,32 0,15 Z" fill="url(#flap)"/>
  </svg>
</section>

<section class="card card-front">
  <div class="brand">NORTHVALE</div>
  <div class="short-rule"></div>
  <div class="tagline">STRATEGY. INTELLIGENCE. GROWTH.</div>
</section>

<section class="card card-back">
  <div class="artwork" role="img" aria-label="Flowing blue ribbon artwork"></div>
  <div class="details">
    <div class="name">GRAHAM HOLLOWAY</div>
    <div class="role">FOUNDER &amp; PRINCIPAL</div>
    <ul class="contact">
      <li><svg viewBox="0 0 10 10"><path d="M2,1 L4,1 L4.6,3 L3.5,4 C4,5.3 4.8,6 6,6.5 L7,5.4 L9,6 L9,8 C5,8.5 1.5,5 2,1 Z" fill="none" stroke="#1e6fd0" stroke-width="0.9"/></svg>+1 617 555 0182</li>
      <li><svg viewBox="0 0 10 10"><rect x="1" y="2" width="8" height="6" fill="none" stroke="#1e6fd0" stroke-width="0.9"/><path d="M1,2 L5,5.5 L9,2" fill="none" stroke="#1e6fd0" stroke-width="0.9"/></svg>graham@northvale.com</li>
      <li><svg viewBox="0 0 10 10"><path d="M5,9.5 C2,6 2,4.5 2,4 A3,3 0 0 1 8,4 C8,4.5 8,6 5,9.5 Z" fill="none" stroke="#1e6fd0" stroke-width="0.9"/><circle cx="5" cy="4" r="1.1" fill="#1e6fd0"/></svg>480 Harlow Street<br>Boston, MA 02116</li>
      <li class="web"><svg viewBox="0 0 10 10"><circle cx="5" cy="5" r="4" fill="none" stroke="#1e6fd0" stroke-width="0.9"/><path d="M1,5 H9 M5,1 C3,3.5 3,6.5 5,9 C7,6.5 7,3.5 5,1" fill="none" stroke="#1e6fd0" stroke-width="0.7"/></svg>northvale.com</li>
    </ul>
  </div>
</section>
</body>
</html>
```